Menu Design Project

We are Brass Lantern Runners a multiple restaurant delivery service. I am looking for a tri-fold, take out style menu. On the front, at the TOP I would like the menu to say "WE DELIVER!" There will be 4 restaurants that I am promoting, so each restaurant will have 1 panel in the menu.
The back of the tri-fold should incorporate an area for postage and address, since i will be mailing these pieces. Also on the back there should be the ordering instructions that will be included in the files.
I would like for the front to have either pictures of food, the logos of the restaurants, our logo, or a combination of the three. Menu items and prices will be input by me. We just need a template designed.

Size= 11" X 17"
We are looking to make a decision today or tomorrow at the latest.

Industry/Entity Type

Restaurant

Requirements
Must have
• We are mailing these through block blanket flyer drop. Must have an area for address label and postage.

"We Deliver" on front of tri-fold, at the top.
Should not have
• Do not use all of the food picks(Unless it looks Awesome). The files are so that you have the options of food picks

```html
<!DOCTYPE html>
<html lang="en">
<head>
<meta charset="utf-8">
<title>We Deliver – Brass Lantern Runners Menu Front</title>
<link rel="stylesheet" href="https://fonts.googleapis.com/css2?family=Cinzel:wght@400;600&family=Indie+Flower&family=Roboto:wght@400;700&display=swap">
<style>
  :root {
    --page-bg: #e6e1d9;
    --paper: #ffffff;
    --brand-red: #c10a12;
    --maroon: #7a1e2c;
    --rose: #c98d96;
    --band-blue: #2358a0;
    --panel-blue: #6088b9;
    --pill-blue: #8fa9d2;
    --logo-dark: #1d1d1f;
    --text-light: #ffffff;
  }
  * { box-sizing: border-box; margin: 0; padding: 0; }
  html, body { width: 1200px; height: 1000px; overflow: hidden; }
  body { background: var(--page-bg); position: relative; font-family: "Roboto", sans-serif; }

  .menu-front {
    position: absolute; left: 120px; top: 160px; width: 960px; height: 678px;
    background: var(--paper); overflow: hidden;
    box-shadow: 0 4px 18px rgba(0,0,0,.18);
  }

  .photo { position: absolute; border: 2px solid var(--maroon); }
  .photo--pizza { border: none; background: linear-gradient(160deg, #d8893f 0 30%, #c6401f 30% 70%, #e9c48a 70%); }
  .photo--samosa { background: linear-gradient(180deg, #7d9a45 0 40%, #c98a3a 40%); }
  .photo--lasagna { background: linear-gradient(180deg, #2a100c 0 35%, #b65a2a 35% 70%, #3a1410 70%); }
  .photo--curry { background: linear-gradient(180deg, #e6d7bd 0 40%, #c2531f 40% 80%, #8a8a8a 80%); }
  .photo--pasta { background: linear-gradient(180deg, #2f5b22 0 25%, #ede6dc 25% 40%, #b8371f 40% 80%, #2f5b22 80%); }
  .photo--burger { background: linear-gradient(180deg, #4a3a30 0 30%, #c89a5c 30% 50%, #5a2f1a 50% 75%, #d9c4a0 75%); }
  .photo--steak { background: linear-gradient(180deg, #3a2a22 0 40%, #7a3a22 40% 85%, #d8cdbd 85%); }
  .photo--salad { background: linear-gradient(180deg, #b08a55 0 50%, #7a8e3a 50%); border-color: var(--rose); border-width: 3px; }
  .photo--ribs { background: linear-gradient(180deg, #3a2418 0 35%, #a84e25 35% 80%, #4f6a2a 80%); }
  .photo--sandwich { background: linear-gradient(180deg, #6a4a2a 0 25%, #e7d6b5 25% 40%, #a8553a 40% 70%, #e8d9be 70%); }

  .brand-faint {
    position: absolute; left: 395px; top: 5px; width: 150px; height: 100px;
    border: 3px solid rgba(201,141,150,.22);
  }
  .headline {
    position: absolute; left: 0; width: 960px; top: 22px; text-align: center;
    font-family: "Cinzel", serif; font-weight: 400; font-size: 62px;
    letter-spacing: 14px; color: var(--brand-red); line-height: 1;
  }

  .logo-band { position: absolute; left: 0; top: 108px; width: 960px; height: 62px; background: var(--band-blue); border-top: 2px solid var(--maroon); border-bottom: 2px solid var(--maroon); }
  .logo-band__pill { position: absolute; top: 6px; height: 48px; background: var(--pill-blue); border-radius: 24px; }
  .band-shadow { position: absolute; left: 0; top: 170px; width: 960px; height: 28px; background: linear-gradient(#cfcfcf, #ffffff); }

  .partner-logo {
    position: absolute; background: var(--logo-dark); border: 2px solid var(--maroon);
    display: flex; flex-direction: column; align-items: center; justify-content: center; gap: 8px;
    color: var(--text-light); font-family: "Roboto", sans-serif; font-weight: 700; text-align: center; padding: 4px;
  }
  .partner-logo__mark { width: 14px; height: 14px; background: var(--text-light); }

  .menu-frame { position: absolute; left: 30px; top: 198px; width: 898px; height: 480px; background: var(--band-blue); }
  .side-pill { position: absolute; top: 198px; width: 56px; height: 500px; background: var(--pill-blue); border-radius: 28px; }
  .menu-panel { position: absolute; left: 93px; top: 198px; width: 762px; height: 354px; background: var(--panel-blue); border-radius: 130px 130px 90px 90px / 70px 70px 70px 70px; }
  .panel-divider { position: absolute; top: 198px; width: 4px; height: 349px; background: var(--paper); }
  .bottom-fade { position: absolute; left: 105px; top: 552px; width: 748px; height: 126px; background: linear-gradient(#cfcfcf, #ffffff 45%); }

  .menu-column { position: absolute; top: 214px; width: 240px; text-align: center; color: var(--text-light); }
  .menu-column__title { font-family: "Cinzel", serif; font-weight: 400; font-size: 19px; letter-spacing: 3px; text-decoration: underline; text-decoration-thickness: 1px; text-underline-offset: 4px; }
  .menu-column__placeholder { margin-top: 124px; font-family: "Indie Flower", cursive; font-size: 19px; letter-spacing: 2px; }

  .ribbon { position: absolute; left: 60px; top: 490px; }
  .brand-box {
    position: absolute; left: 407px; top: 538px; width: 149px; height: 99px; background: var(--paper);
    border: 3px solid var(--rose); display: flex; align-items: center; justify-content: center;
    font-family: "Cinzel", serif; font-weight: 600; font-size: 15px; line-height: 1.15; color: var(--brand-red); text-align: center; padding: 6px;
  }
</style>
</head>
<body>
<main class="menu-front">
  <div class="photo photo--pizza" style="left:0;top:0;width:148px;height:108px" role="img" aria-label="Pepperoni pizza"></div>
  <div class="photo photo--pizza" style="left:812px;top:0;width:148px;height:108px" role="img" aria-label="Pepperoni pizza"></div>
  <div class="brand-faint" aria-hidden="true"></div>
  <h1 class="headline">WE DELIVER</h1>

  <div class="logo-band">
    <span class="logo-band__pill" style="left:2px;width:103px"></span>
    <span class="logo-band__pill" style="left:198px;width:120px"></span>
    <span class="logo-band__pill" style="left:642px;width:88px"></span>
    <span class="logo-band__pill" style="left:855px;width:103px"></span>
  </div>
  <div class="band-shadow"></div>

  <div class="partner-logo" style="left:105px;top:78px;width:93px;height:120px;font-size:15px"><span class="partner-logo__mark"></span>Slate Ridge Alehouse</div>
  <div class="partner-logo" style="left:320px;top:108px;width:320px;height:62px;font-size:26px;background:#050505">Saffron Court Kitchen</div>
  <div class="partner-logo" style="left:730px;top:78px;width:125px;height:120px;font-size:17px;background:#3a3a3c"><span class="partner-logo__mark"></span>Marlow's Grill House</div>

  <div class="menu-frame"></div>
  <div class="side-pill" style="left:40px"></div>
  <div class="side-pill" style="left:863px"></div>
  <div class="bottom-fade"></div>
  <div class="menu-panel"></div>
  <div class="panel-divider" style="left:353px"></div>
  <div class="panel-divider" style="left:606px"></div>

  <section class="menu-column" style="left:118px"><h2 class="menu-column__title">MENU</h2><p class="menu-column__placeholder">YOUR MENU HERE!</p></section>
  <section class="menu-column" style="left:357px"><h2 class="menu-column__title">MENU</h2><p class="menu-column__placeholder">YOUR MENU HERE!</p></section>
  <section class="menu-column" style="left:610px"><h2 class="menu-column__title">MENU</h2><p class="menu-column__placeholder">YOUR MENU HERE!</p></section>

  <div class="photo photo--samosa" style="left:10px;top:261px;width:108px;height:71px" role="img" aria-label="Samosas with salad"></div>
  <div class="photo photo--lasagna" style="left:10px;top:361px;width:108px;height:82px" role="img" aria-label="Layered lasagna on a plate"></div>
  <div class="photo photo--curry" style="left:840px;top:255px;width:108px;height:72px" role="img" aria-label="Curry bowl with naan"></div>
  <div class="photo photo--pasta" style="left:840px;top:356px;width:108px;height:82px" role="img" aria-label="Pasta in tomato sauce"></div>

  <div class="photo photo--burger" style="left:67px;top:518px;width:149px;height:132px" role="img" aria-label="Burger topped with fried onions"></div>
  <div class="photo photo--steak" style="left:265px;top:585px;width:90px;height:65px" role="img" aria-label="Grilled steak"></div>
  <div class="photo photo--ribs" style="left:606px;top:585px;width:108px;height:65px" role="img" aria-label="Barbecue ribs"></div>
  <div class="photo photo--sandwich" style="left:763px;top:518px;width:133px;height:132px" role="img" aria-label="Stacked deli sandwich"></div>

  <svg class="ribbon" width="850" height="130" viewBox="0 0 850 130" aria-hidden="true">
    <path d="M7 5 C 120 95, 300 112, 420 112 C 560 112, 730 95, 836 5 L 836 30 C 730 110, 560 128, 420 128 C 300 128, 120 110, 7 30 Z" fill="var(--maroon)"/>
    <path d="M7 5 C 120 80, 300 96, 420 98 C 560 96, 730 80, 836 5 C 730 92, 560 108, 420 110 C 300 108, 120 92, 7 5 Z" fill="var(--rose)"/>
  </svg>

  <div class="photo photo--salad" style="left:382px;top:523px;width:198px;height:130px" role="img" aria-label="Plated salad"></div>
  <div class="brand-box">Brass Lantern Runners</div>
</main>
</body>
</html>
```